lawn sign

Lawn Sign
Roofing Gutters Windows

Target Market(s)

roofing

Font styles to use
Sans Serif

Colors
86cfc6
33a6d7
fbee3f
faa54b

Requirements
Must have
• my logo
Nice to have
• designer for now

```html
<!DOCTYPE html>
<html lang="en">
<head>
<meta charset="utf-8">
<title>Marlowe Lawn Sign</title>
<link rel="stylesheet" href="https://fonts.googleapis.com/css2?family=Cinzel:wght@400;700&display=swap">
<style>
  :root {
    --page-bg: #eceeea;
    --blue-deep: #1c3f86;
    --blue-mid: #1d6fb8;
    --blue-light: #2d8fd0;
    --green: #4f9a35;
    --green-bright: #8cc63f;
    --green-dark: #1a9a48;
    --brand-text: #4f9f38;
    --brand-teal: #1f8f8c;
    --white: #ffffff;
    --ink: #111111;
  }
  html, body {
    margin: 0;
    padding: 0;
    width: 1200px;
    height: 1199px;
    overflow: hidden;
    background: var(--page-bg);
  }
  .lawn-sign {
    position: absolute;
    left: 0;
    top: 146px;
    width: 1200px;
    height: 907px;
    display: block;
  }
  .service-title {
    font-family: "Cinzel", serif;
    font-weight: 700;
    font-size: 50px;
    letter-spacing: 1px;
  }
  .brand-name {
    font-family: "Cinzel", serif;
    font-weight: 400;
    fill: var(--brand-text);
  }
  .brand-name-main {
    fill: var(--brand-teal);
  }
  .email-text {
    font-family: "Cinzel", serif;
    font-weight: 700;
    font-size: 24px;
    fill: var(--white);
  }
  .phone-text {
    font-family: "Cinzel", serif;
    font-weight: 400;
    font-size: 46px;
    fill: var(--white);
  }
</style>
</head>
<body>
<svg class="lawn-sign" viewBox="0 0 1200 907" xmlns="http://www.w3.org/2000/svg">
  <defs>
    <linearGradient id="panelBlue" x1="0" y1="0" x2="0" y2="1">
      <stop offset="0" stop-color="var(--blue-light)"/>
      <stop offset="1" stop-color="var(--blue-deep)"/>
    </linearGradient>
    <linearGradient id="panelGrey" x1="0" y1="0" x2="0" y2="1">
      <stop offset="0" stop-color="#d6d9dc"/>
      <stop offset="1" stop-color="#eef0f1"/>
    </linearGradient>
    <linearGradient id="arcBlue" x1="0" y1="0" x2="1" y2="0">
      <stop offset="0" stop-color="var(--blue-light)"/>
      <stop offset="1" stop-color="var(--blue-deep)"/>
    </linearGradient>
    <linearGradient id="arcGreen" x1="0" y1="0" x2="1" y2="0">
      <stop offset="0" stop-color="var(--green-bright)"/>
      <stop offset="1" stop-color="var(--green-dark)"/>
    </linearGradient>
    <linearGradient id="ribbonBlue" x1="0" y1="0" x2="1" y2="0">
      <stop offset="0" stop-color="var(--blue-mid)"/>
      <stop offset="1" stop-color="var(--blue-deep)"/>
    </linearGradient>
    <linearGradient id="ribbonGreen" x1="0" y1="0" x2="1" y2="0">
      <stop offset="0" stop-color="var(--green-bright)"/>
      <stop offset="1" stop-color="var(--green-dark)"/>
    </linearGradient>
  </defs>

  <rect class="panel panel-roofing" x="0" y="0" width="400" height="560" fill="url(#panelBlue)" role="img" aria-label="Photo of a house roof"/>
  <rect class="panel panel-windows" x="400" y="0" width="400" height="430" fill="url(#panelGrey)" role="img" aria-label="Photo of house siding and windows"/>
  <rect class="panel panel-gutters" x="800" y="0" width="400" height="720" fill="url(#panelBlue)" role="img" aria-label="Photo of a gutter downspout"/>

  <text class="service-title" x="200" y="213" text-anchor="middle" fill="var(--white)">Roofing</text>
  <text class="service-title" x="600" y="213" text-anchor="middle" fill="var(--ink)">Windows</text>
  <text class="service-title" x="1000" y="213" text-anchor="middle" fill="var(--white)">Gutters</text>

  <path class="arc-blue" d="M0,428 C300,372 720,350 1200,575 L1200,907 L0,907 Z" fill="url(#arcBlue)"/>
  <path class="arc-green" d="M0,455 C300,410 720,385 1200,640 L1200,907 L0,907 Z" fill="url(#arcGreen)"/>
  <path class="sign-body" d="M0,478 C300,440 720,420 1200,708 L1200,907 L0,907 Z" fill="var(--white)"/>

  <g class="icon icon-roofing">
    <circle cx="200" cy="430" r="76" fill="var(--green)" stroke="var(--white)" stroke-width="6"/>
    <path d="M158,457 L200,418 L242,457 L242,445 L222,426 L222,402 L210,402 L210,415 L200,405 L158,445 Z" fill="var(--white)"/>
    <rect x="184" y="440" width="28" height="18" fill="var(--white)"/>
    <rect x="192" y="444" width="5" height="4" fill="var(--green)"/>
    <rect x="199" y="444" width="5" height="4" fill="var(--green)"/>
    <rect x="192" y="450" width="5" height="4" fill="var(--green)"/>
    <rect x="199" y="450" width="5" height="4" fill="var(--green)"/>
  </g>
  <g class="icon icon-windows">
    <circle cx="602" cy="433" r="76" fill="var(--green)" stroke="var(--white)" stroke-width="6"/>
    <rect x="566" y="398" width="33" height="33" fill="var(--white)"/>
    <rect x="605" y="398" width="33" height="33" fill="var(--white)"/>
    <rect x="566" y="437" width="33" height="33" fill="var(--white)"/>
    <rect x="605" y="437" width="33" height="33" fill="var(--white)"/>
  </g>
  <g class="icon icon-gutters">
    <circle cx="1000" cy="553" r="76" fill="var(--green)" stroke="var(--white)" stroke-width="6"/>
    <path d="M960,528 L1040,528 L1034,546 L966,546 Z" fill="var(--white)"/>
    <path d="M1000,546 L1014,546 L1014,568 L1002,568 L1002,590 L988,590 L988,560 L1000,560 Z" fill="var(--white)"/>
  </g>

  <circle class="brand-mark" cx="200" cy="660" r="128" fill="#e4f2f8"/>
  <text class="brand-name brand-name-main" x="688" y="770" text-anchor="end" font-size="58">MARLOWE</text>
  <text class="brand-name" x="688" y="825" text-anchor="end" font-size="40">Restoration</text>
  <text class="brand-name" x="688" y="870" text-anchor="end" font-size="40">Remodeling Group LLC</text>

  <g class="contact contact-email">
    <path d="M755,724 L1200,724 L1200,795 L755,795 L725,760 Z" fill="url(#ribbonBlue)"/>
    <circle cx="788" cy="760" r="20" fill="none" stroke="var(--white)" stroke-width="2.5"/>
    <rect x="778" y="753" width="20" height="14" rx="1.5" fill="var(--white)"/>
    <path d="M778,754 L788,761 L798,754" fill="none" stroke="var(--blue-mid)" stroke-width="1.8"/>
    <text class="email-text" x="822" y="769" textLength="350" lengthAdjust="spacingAndGlyphs">INFO@MARLOWELLC.COM</text>
  </g>
  <g class="contact contact-phone">
    <path d="M755,797 L1200,797 L1200,868 L755,868 L725,832 Z" fill="url(#ribbonGreen)"/>
    <circle cx="788" cy="832" r="20" fill="none" stroke="var(--white)" stroke-width="2.5"/>
    <path d="M780,823 C778,832 786,842 796,842 L798,837 L793,834 L790,836 C786,834 784,831 783,828 L785,825 L783,820 Z" fill="var(--white)"/>
    <text class="phone-text" x="822" y="849" textLength="350" lengthAdjust="spacingAndGlyphs">(555) 014-7730</text>
  </g>
</svg>
</body>
</html>
```